Powerpoint template & style design project

KMaldrey Consulting is an IT technology firm specializing in mobility and telecommunications applications. We provide technical consulting to global companies that want to build mobile applications and take critical business applications and move them into the cloud.
We would like to see designs that use the color blue. The final design should communicate confidence, agility and speak to technology focused customers. Forward progress and/or motion should be conveyed.

Target Market(s)

Government customers and large enterprise companies

Industry/Entity Type

Telecommunications

Font styles to use
Sans Serif

Colors
0555a3

Requirements
Must have
• different slides: Cover page, title slide, main content, transition slide, close out slide..

```html
<!DOCTYPE html>
<html lang="en">
<head>
<meta charset="utf-8">
<title>KMaldrey Consulting – Presentation Template</title>
<link rel="stylesheet" href="https://fonts.googleapis.com/css2?family=Arimo:wght@400;700&display=swap">
<style>
  :root {
    --canvas-grey: #cbcbcb;
    --slide-white: #ffffff;
    --navy: #031a40;
    --navy-deep: #02163a;
    --ink: #000000;
    --silver: #c9cbcf;
    --silver-soft: #d9dbe0;
    --photo-dark: #04142e;
    --photo-mid: #0b3f86;
    --photo-light: #6fb6ee;
  }
  * { box-sizing: border-box; margin: 0; padding: 0; }
  html, body { width: 1200px; height: 1000px; overflow: hidden; }
  body {
    background: var(--canvas-grey);
    font-family: "Arimo", Arial, sans-serif;
    position: relative;
  }
  .slide {
    position: absolute;
    width: 550px;
    height: 456px;
    background: var(--slide-white);
    overflow: hidden;
  }
  .slide--cover   { left: 20px;  top: 20px; }
  .slide--content { left: 631px; top: 20px; width: 549px; }
  .slide--image   { left: 20px;  top: 524px; }
  .slide--closing { left: 631px; top: 524px; width: 549px; background: var(--navy-deep); }

  .footer-band {
    position: absolute;
    left: 0; bottom: 0;
    width: 100%;
    height: 100px;
    display: block;
  }

  .footer-brand {
    position: absolute;
    right: 30px;
    bottom: 20px;
    text-align: center;
    color: var(--silver);
  }
  .footer-brand__name {
    font-weight: 700;
    font-size: 13px;
    letter-spacing: -0.2px;
    white-space: nowrap;
  }
  .footer-brand__tagline {
    font-size: 5px;
    letter-spacing: 1.2px;
    margin-top: 2px;
    white-space: nowrap;
  }

  .cover-title {
    position: absolute;
    left: 38px; right: 0;
    top: 133px;
    text-align: center;
    font-weight: 700;
    font-size: 34px;
    line-height: 41px;
    color: var(--ink);
  }

  .content-text {
    position: absolute;
    left: 31px;
    top: 157px;
    white-space: nowrap;
    font-weight: 700;
    font-size: 20px;
    line-height: 23px;
    color: var(--ink);
  }

  .image-area {
    position: absolute;
    left: 56px;
    top: 39px;
    width: 434px;
    height: 288px;
    background:
      radial-gradient(ellipse 55% 35% at 60% 50%, var(--photo-light) 0%, rgba(111,182,238,0) 70%),
      linear-gradient(135deg, var(--photo-dark) 0%, var(--photo-mid) 55%, var(--photo-dark) 100%);
  }

  .closing-brand {
    position: absolute;
    left: 0; right: 0;
    top: 236px;
    text-align: center;
    color: var(--silver);
  }
  .closing-brand__name {
    font-weight: 700;
    font-size: 40px;
    letter-spacing: -0.5px;
  }
  .closing-brand__tagline {
    font-size: 15px;
    letter-spacing: 3px;
    margin-top: 4px;
    color: var(--silver-soft);
  }
  .closing-note {
    position: absolute;
    right: 42px;
    bottom: 30px;
    font-size: 20px;
    color: var(--silver-soft);
  }
</style>
</head>
<body>

<svg width="0" height="0" style="position:absolute" aria-hidden="true">
  <defs>
    <g id="footer-band-shape">
      <path d="M0 20 Q275 0 550 20 L550 100 L0 100 Z" fill="var(--navy)"/>
      <path d="M0 34 Q275 16 550 34" fill="none" stroke="var(--slide-white)" stroke-width="3"/>
    </g>
  </defs>
</svg>

<section class="slide slide--cover">
  <h1 class="cover-title">KMaldrey Consulting<br>Welcome to presentation<br>April 2015</h1>
  <svg class="footer-band" viewBox="0 0 550 100" preserveAspectRatio="none" aria-hidden="true"><use href="#footer-band-shape"/></svg>
  <div class="footer-brand">
    <div class="footer-brand__name">KMaldrey Consulting</div>
    <div class="footer-brand__tagline">MOBILITY &amp; TELECOMMUNICATIONS</div>
  </div>
</section>

<section class="slide slide--content">
  <p class="content-text">we specialize in:Mobility and Telecommunications:<br>Strategy, Planning &amp; ManagementPeople,<br>Process and Technology Solutions</p>
  <svg class="footer-band" viewBox="0 0 550 100" preserveAspectRatio="none" aria-hidden="true"><use href="#footer-band-shape"/></svg>
  <div class="footer-brand">
    <div class="footer-brand__name">KMaldrey Consulting</div>
    <div class="footer-brand__tagline">MOBILITY &amp; TELECOMMUNICATIONS</div>
  </div>
</section>

<section class="slide slide--image">
  <div class="image-area" role="img" aria-label="Photo of a smartphone showing a globe, with glowing blue data streams flowing to the right"></div>
  <svg class="footer-band" viewBox="0 0 550 100" preserveAspectRatio="none" aria-hidden="true"><use href="#footer-band-shape"/></svg>
  <div class="footer-brand">
    <div class="footer-brand__name">KMaldrey Consulting</div>
    <div class="footer-brand__tagline">MOBILITY &amp; TELECOMMUNICATIONS</div>
  </div>
</section>

<section class="slide slide--closing">
  <div class="closing-brand">
    <div class="closing-brand__name">KMaldrey Consulting</div>
    <div class="closing-brand__tagline">MOBILITY &amp; TELECOMMUNICATIONS</div>
  </div>
  <p class="closing-note">power point example</p>
</section>

</body>
</html>
```